Meridale Legal Letterhead for Law firm must be modern and use the logo I uploaded.

Hello I want a clean modern professional letterhead for my law firm Meridale Legal. A logo has already been created and all files have been uploaded. The information for the firm can be given through message. Please use the logo that has already been created. Please also use the color scheme of that logo. (blue and white).

Target Market(s)

General Public

Industry/Entity Type

Law Firm

Colors

Designer to choose colors to be used in the design.

Requirements
Must have
• This must be a modern professional letterhead
Nice to have
• My logo that is included in file form
Should not have
• Should not have logo that is not the one I uploaded.

```html
<!DOCTYPE html>
<html lang="en">
<head>
<meta charset="utf-8">
<title>Meridale Legal Letterhead</title>
<link href="https://fonts.googleapis.com/css2?family=Open+Sans:wght@400;600&family=Roboto:wght@400&display=swap" rel="stylesheet">
<style>
  :root {
    --navy: #2f3462;
    --navy-soft: #3b416e;
    --ink: #44475a;
    --paper: #ffffff;
    --backdrop: #c9c9c9;
    --sig-tint: #e6e7ef;
  }
  * { box-sizing: border-box; margin: 0; padding: 0; }
  html, body {
    width: 1200px; height: 900px; overflow: hidden;
    background: var(--backdrop);
  }
  .letterhead {
    position: absolute; left: 290px; top: 12px;
    width: 620px; height: 876px;
    background: var(--paper);
    box-shadow: 0 4px 18px rgba(0,0,0,.18);
    font-family: "Open Sans", sans-serif;
    color: var(--ink);
  }
  .letterhead-header {
    position: absolute; left: 52px; right: 52px; top: 48px;
    height: 110px;
  }
  .firm-name {
    position: absolute; left: 0; top: 50px;
    font-family: "Open Sans", sans-serif;
    font-weight: 600; font-size: 15px;
    letter-spacing: 6px; text-transform: uppercase;
    color: var(--navy);
  }
  .contact-block {
    position: absolute; right: 0; top: 22px; width: 150px;
    font-family: "Roboto", sans-serif;
    font-size: 9.5px; line-height: 1.35; color: var(--navy-soft);
  }
  .contact-address { margin-bottom: 4px; }
  .contact-line { display: flex; align-items: center; gap: 5px; }
  .contact-line svg { width: 8px; height: 8px; fill: var(--navy); flex: none; }
  .header-rule {
    position: absolute; left: 52px; right: 52px; top: 168px;
    height: 1.5px; background: var(--navy);
  }
  .letter-body {
    position: absolute; left: 52px; right: 52px; top: 196px;
    font-size: 10.6px; line-height: 1.5; text-align: justify;
  }
  .salutation { margin-bottom: 14px; }
  .letter-body p.paragraph { margin-bottom: 12px; }
  .closing { margin-top: 4px; }
  .signature {
    width: 70px; height: 48px; margin-top: 14px;
    background: linear-gradient(135deg, var(--sig-tint), #f3f4f8);
    border-radius: 3px;
  }
  .footer-band {
    position: absolute; left: 0; right: 0; bottom: 0;
    height: 14px; background: var(--navy);
  }
</style>
</head>
<body>
  <main class="letterhead">
    <header class="letterhead-header">
      <div class="firm-name">Meridale Legal</div>
      <address class="contact-block" style="font-style:normal">
        <div class="contact-address">4280 North Alder Court Suite 12 Fairmont, CO 80214</div>
        <div class="contact-line">
          <svg viewBox="0 0 10 10"><path d="M2 1h2l1 2.5-1.2.8a5 5 0 0 0 2 2l.8-1.2L9 6v2a1 1 0 0 1-1 1A8 8 0 0 1 1 2a1 1 0 0 1 1-1z"/></svg>
          <span>720.555.0148</span>
        </div>
        <div class="contact-line">
          <svg viewBox="0 0 10 10"><path d="M0 2h10v6H0z M0 2l5 3.5L10 2" fill="none" stroke="#2f3462" stroke-width="1.2"/></svg>
          <span>info@meridalelegal.com</span>
        </div>
        <div class="contact-line">
          <svg viewBox="0 0 10 10"><circle cx="5" cy="5" r="4.5"/></svg>
          <span>www.meridalelegal.com</span>
        </div>
      </address>
    </header>
    <div class="header-rule"></div>

    <section class="letter-body">
      <p class="salutation">Dear customer,</p>
      <p class="paragraph">Lorem ipsum dolor sit amet, consectetur adipisicing elit, sed do eiusmod tempor incididunt ut labore et dolore magna aliqua. Ut enim ad minim veniam, quis nostrud exercitation ullamco laboris nisi ut aliquip ex ea commodo consequat. Duis aute irure dolor in reprehenderit in voluptate velit esse cillum dolore eu fugiat nulla pariatur. Excepteur sint occaecat cupidatat non proident, sunt in culpa qui officia deserunt mollit anim id est laborum.</p>
      <p class="paragraph">Lorem ipsum dolor sit amet, consectetur adipisicing elit, sed do eiusmod tempor incididunt ut labore et dolore magna aliqua. Ut enim ad minim veniam, quis nostrud exercitation ullamco laboris nisi ut aliquip ex ea commodo consequat. Duis aute irure dolor in reprehenderit in voluptate velit esse cillum dolore eu fugiat nulla pariatur. Excepteur sint occaecat cupidatat non proident, sunt in culpa qui officia deserunt mollit anim id est laborum.</p>
      <p class="paragraph">Lorem ipsum dolor sit amet, consectetur adipisicing elit, sed do eiusmod tempor incididunt ut labore et dolore magna aliqua. Ut enim ad minim veniam, quis nostrud exercitation ullamco laboris nisi ut aliquip ex ea commodo consequat. Duis aute irure dolor in reprehenderit in voluptate velit esse cillum dolore eu fugiat nulla pariatur. Excepteur sint occaecat cupidatat non proident, sunt in culpa qui officia deserunt mollit anim id est laborum.</p>
      <p class="paragraph">Lorem ipsum dolor sit amet, consectetur adipisicing elit, sed do eiusmod tempor incididunt ut labore et dolore magna aliqua. Ut enim ad minim veniam, quis nostrud exercitation ullamco laboris nisi ut aliquip ex ea commodo consequat. Duis aute irure dolor in reprehenderit.</p>
      <p class="closing">Yours Sincerely,</p>
      <div class="signature" role="img" aria-label="Handwritten signature of the sender"></div>
    </section>

    <div class="footer-band"></div>
  </main>
</body>
</html>
```